Simple icons/shapes for web application

We'd like 6 icon/shapes, each in 6 different colours. The icons will be used to differentiate documents displayed in a long list. The shapes are circle, square, document, star and shield (all 16Wx16H) and rectangle (32Wx16H) . The colours are Red (#cc0000), Orange (#ff6600), Yellow (#ffcc33), Green (#00cc00), Blue (#0066cc) and Purple (#6633cc). We'd like to see examples of both flat and styled icons (e.g. glassy, graded, bordered, rounded) with transparency where applicable.
Thank you for the submissions so far. If possible could designers submit designs at the intended size (16px high), we're happy to also see an enlarged version but it is really important for us to see them at the size they will be used.

```html
<!DOCTYPE html>
<html lang="en">
<head>
<meta charset="utf-8">
<title>Icon Shapes – Colour Set</title>
<link rel="stylesheet" href="https://fonts.googleapis.com/css2?family=Aleo:wght@400&display=swap">
<style>
  :root {
    --red: #c1401f;
    --blue: #0a5ea6;
    --yellow: #f6bb3b;
    --green: #40b036;
    --orange: #e4661e;
    --purple: #413f8a;
    --ink: #2a2a2a;
    --backdrop-low: #d9d9d9;
    --backdrop-mid: #ececec;
    --backdrop-high: #ffffff;
  }
  html, body {
    margin: 0;
    padding: 0;
    overflow: hidden;
  }
  .sheet {
    position: relative;
    width: 1200px;
    height: 756px;
    overflow: hidden;
    background: var(--backdrop-mid);
    font-family: "Aleo", Georgia, serif;
    color: var(--ink);
  }
  .backdrop, .icon-grid {
    position: absolute;
    inset: 0;
  }
  .label {
    position: absolute;
    font-size: 28px;
    line-height: 1;
    white-space: nowrap;
    transform: translate(-50%, -50%);
  }
  .swatch-red    { fill: var(--red); }
  .swatch-blue   { fill: var(--blue); }
  .swatch-yellow { fill: var(--yellow); }
  .swatch-green  { fill: var(--green); }
  .swatch-orange { fill: var(--orange); }
  .swatch-purple { fill: var(--purple); }
  .star-shape { stroke-linejoin: round; stroke-width: 4; }
  .swatch-red .star-shape, .star.swatch-red    { stroke: var(--red); }
  .star.swatch-blue   { stroke: var(--blue); }
  .star.swatch-yellow { stroke: var(--yellow); }
  .star.swatch-green  { stroke: var(--green); }
  .star.swatch-orange { stroke: var(--orange); }
  .star.swatch-purple { stroke: var(--purple); }
  .star { stroke-linejoin: round; stroke-width: 4; }
</style>
</head>
<body>
<main class="sheet">

  <svg class="backdrop" width="1200" height="756" viewBox="0 0 1200 756" aria-hidden="true">
    <defs>
      <linearGradient id="floor" x1="0" y1="0" x2="0" y2="1">
        <stop offset="0" stop-color="#dedede"/>
        <stop offset="1" stop-color="#ebebeb"/>
      </linearGradient>
      <radialGradient id="glow" cx="600" cy="220" r="700" gradientUnits="userSpaceOnUse">
        <stop offset="0" stop-color="#ffffff"/>
        <stop offset="0.55" stop-color="#f7f7f7"/>
        <stop offset="1" stop-color="#e9e9e9"/>
      </radialGradient>
      <radialGradient id="lowerGlow" cx="600" cy="560" r="620" gradientUnits="userSpaceOnUse">
        <stop offset="0" stop-color="#f3f3f3"/>
        <stop offset="1" stop-color="#dcdcdc"/>
      </radialGradient>
    </defs>
    <rect width="1200" height="756" fill="url(#lowerGlow)"/>
    <ellipse cx="600" cy="-400" rx="1100" ry="870" fill="url(#glow)"/>
  </svg>

  <!-- column headings -->
  <span class="label col-heading" style="left:313px; top:90px;">Red</span>
  <span class="label col-heading" style="left:462px; top:90px;">Blue</span>
  <span class="label col-heading" style="left:611px; top:90px;">Yellow</span>
  <span class="label col-heading" style="left:760px; top:90px;">Green</span>
  <span class="label col-heading" style="left:908px; top:90px;">Orange</span>
  <span class="label col-heading" style="left:1057px; top:90px;">Purple</span>

  <!-- row headings -->
  <span class="label row-heading" style="left:164px; top:154px;">Square</span>
  <span class="label row-heading" style="left:184px; top:255px;">Circle</span>
  <span class="label row-heading" style="left:177px; top:355px;">Star</span>
  <span class="label row-heading" style="left:151px; top:454px;">Document</span>
  <span class="label row-heading" style="left:170px; top:553px;">Shield</span>
  <span class="label row-heading" style="left:158px; top:651px;">Rectangle</span>

  <svg class="icon-grid" width="1200" height="756" viewBox="0 0 1200 756" role="img" aria-label="Six icon shapes shown in six colours">
    <defs>
      <symbol id="icon-square" viewBox="0 0 62 62">
        <rect width="62" height="62"/>
      </symbol>
      <symbol id="icon-circle" viewBox="0 0 62 62">
        <circle cx="31" cy="31" r="31"/>
      </symbol>
      <symbol id="icon-star" viewBox="-32 -32 64 64" overflow="visible">
        <polygon points="0,-28 7,-9.6 27,-8.8 11.3,3.7 16.8,23 0,12 -16.8,23 -11.3,3.7 -27,-8.8 -7,-9.6"/>
      </symbol>
      <symbol id="icon-document" viewBox="0 0 48 62">
        <path d="M0,0 H35 L48,13 V62 H0 Z"/>
        <g fill="#ffffff">
          <path d="M36,3 L45,12 H36 Z"/>
          <rect x="6" y="6" width="18" height="8"/>
          <rect x="6" y="20" width="36" height="2.6"/>
          <rect x="6" y="26.5" width="36" height="2.6"/>
          <rect x="6" y="33" width="36" height="2.6"/>
          <rect x="6" y="39.5" width="36" height="2.6"/>
          <rect x="6" y="46" width="36" height="2.6"/>
          <rect x="6" y="52.5" width="36" height="2.6"/>
        </g>
      </symbol>
      <symbol id="icon-shield" viewBox="0 0 52 60">
        <path d="M0,7 Q14,7 26,0 Q38,7 52,7 V30 Q52,50 26,60 Q0,50 0,30 Z"/>
      </symbol>
      <symbol id="icon-rectangle" viewBox="0 0 123 62">
        <rect width="123" height="62"/>
      </symbol>
    </defs>

    <g class="row-square">
      <use href="#icon-square" class="swatch-red"    x="282"  y="124" width="62" height="62"/>
      <use href="#icon-square" class="swatch-blue"   x="431"  y="124" width="62" height="62"/>
      <use href="#icon-square" class="swatch-yellow" x="580"  y="124" width="62" height="62"/>
      <use href="#icon-square" class="swatch-green"  x="729"  y="124" width="62" height="62"/>
      <use href="#icon-square" class="swatch-orange" x="877"  y="124" width="62" height="62"/>
      <use href="#icon-square" class="swatch-purple" x="1026" y="124" width="62" height="62"/>
    </g>

    <g class="row-circle">
      <use href="#icon-circle" class="swatch-red"    x="282"  y="224" width="62" height="62"/>
      <use href="#icon-circle" class="swatch-blue"   x="431"  y="224" width="62" height="62"/>
      <use href="#icon-circle" class="swatch-yellow" x="580"  y="224" width="62" height="62"/>
      <use href="#icon-circle" class="swatch-green"  x="729"  y="224" width="62" height="62"/>
      <use href="#icon-circle" class="swatch-orange" x="877"  y="224" width="62" height="62"/>
      <use href="#icon-circle" class="swatch-purple" x="1026" y="224" width="62" height="62"/>
    </g>

    <g class="row-star">
      <use href="#icon-star" class="star swatch-red"    x="281"  y="323" width="64" height="64"/>
      <use href="#icon-star" class="star swatch-blue"   x="430"  y="323" width="64" height="64"/>
      <use href="#icon-star" class="star swatch-yellow" x="579"  y="323" width="64" height="64"/>
      <use href="#icon-star" class="star swatch-green"  x="728"  y="323" width="64" height="64"/>
      <use href="#icon-star" class="star swatch-orange" x="876"  y="323" width="64" height="64"/>
      <use href="#icon-star" class="star swatch-purple" x="1025" y="323" width="64" height="64"/>
    </g>

    <g class="row-document">
      <use href="#icon-document" class="swatch-red"    x="290"  y="417" width="48" height="62"/>
      <use href="#icon-document" class="swatch-blue"   x="439"  y="417" width="48" height="62"/>
      <use href="#icon-document" class="swatch-yellow" x="587"  y="417" width="48" height="62"/>
      <use href="#icon-document" class="swatch-green"  x="736"  y="417" width="48" height="62"/>
      <use href="#icon-document" class="swatch-orange" x="885"  y="417" width="48" height="62"/>
      <use href="#icon-document" class="swatch-purple" x="1033" y="417" width="48" height="62"/>
    </g>

    <g class="row-shield">
      <use href="#icon-shield" class="swatch-red"    x="288"  y="512" width="52" height="60"/>
      <use href="#icon-shield" class="swatch-blue"   x="436"  y="512" width="52" height="60"/>
      <use href="#icon-shield" class="swatch-yellow" x="585"  y="512" width="52" height="60"/>
      <use href="#icon-shield" class="swatch-green"  x="734"  y="512" width="52" height="60"/>
      <use href="#icon-shield" class="swatch-orange" x="882"  y="512" width="52" height="60"/>
      <use href="#icon-shield" class="swatch-purple" x="1031" y="512" width="52" height="60"/>
    </g>

    <g class="row-rectangle">
      <use href="#icon-rectangle" class="swatch-red"    x="252" y="615" width="123" height="62"/>
      <use href="#icon-rectangle" class="swatch-blue"   x="400" y="615" width="123" height="62"/>
      <use href="#icon-rectangle" class="swatch-yellow" x="549" y="615" width="123" height="62"/>
      <use href="#icon-rectangle" class="swatch-green"  x="698" y="615" width="123" height="62"/>
      <use href="#icon-rectangle" class="swatch-orange" x="847" y="615" width="123" height="62"/>
      <use href="#icon-rectangle" class="swatch-purple" x="995" y="615" width="123" height="62"/>
    </g>
  </svg>

</main>
</body>
</html>
```